Create Bourbon label for Craft Distillery located in the Foothills of NC.

Need to create a label for a craft bourbon. The brand name is Brookfen. Looking for a traditional/vintage bottle label. I have created a concept and would like an expansion of the concept idea (open to artwork outside of concept art as well). I have included the bottle being used. Label area approx 4.25H x 3.5W. With the Brookfen brand name, would like to incorporate trees (native to NC and Appalachia), mountains (mt pano of area included), and sawblade. However, I do not want the sawblade to be the focal point of the design. The word Bourbon, proof, abv, and 750 ml will need to be horizontal. Brookfen and Made in NC can be angled in the design.

Requirements
Must have
• Front Label will need to contain the followingBrand Name = SawmillsBourbon750 ml100 Proof50% ABVAged 3 years

```html
<!DOCTYPE html>
<html lang="en">
<head>
<meta charset="utf-8">
<title>Brookfen Bourbon Label</title>
<link rel="stylesheet" href="https://fonts.googleapis.com/css2?family=Alfa+Slab+One&family=Oswald:wght@500;600&family=Rye&display=swap">
<style>
  :root {
    --paper: #ffffff;
    --ink: #1e2025;
    --copper: #b8733a;
    --copper-dark: #7a4a26;
    --cream: #f6e6d2;
  }
  html, body {
    margin: 0;
    padding: 0;
    width: 1200px;
    height: 931px;
    overflow: hidden;
    background: var(--paper);
  }
  .label {
    display: block;
    width: 1200px;
    height: 931px;
  }
  .brand-name {
    font-family: "Rye", serif;
    font-size: 118px;
    fill: var(--cream);
    letter-spacing: 4px;
  }
  .origin-line {
    font-family: "Oswald", sans-serif;
    font-weight: 600;
    font-size: 30px;
    fill: var(--cream);
    letter-spacing: 1px;
  }
  .spirit-type {
    font-family: "Alfa Slab One", serif;
    font-size: 74px;
    fill: var(--cream);
    letter-spacing: 38px;
  }
  .age-word {
    font-family: "Oswald", sans-serif;
    font-weight: 600;
    font-size: 28px;
    fill: var(--copper);
  }
  .age-number {
    font-family: "Oswald", sans-serif;
    font-weight: 600;
    font-size: 40px;
    fill: var(--cream);
  }
  .spec {
    font-family: "Oswald", sans-serif;
    font-weight: 500;
    font-size: 27px;
    fill: var(--cream);
  }
</style>
</head>
<body>
<svg class="label" viewBox="762 301 1519 1178" xmlns="http://www.w3.org/2000/svg">
  <defs>
    <linearGradient id="scene-tone" x1="0" y1="0" x2="0" y2="1">
      <stop offset="0" stop-color="#8a5a34"/>
      <stop offset="0.6" stop-color="#b8733a"/>
      <stop offset="1" stop-color="#f6e6d2"/>
    </linearGradient>
  </defs>

  <!-- label body and side tabs -->
  <g class="label-body">
    <rect x="1120" y="345" width="805" height="1090" rx="90" fill="var(--ink)"/>
    <path d="M1130 780 L1060 800 Q1030 860 1060 920 L1130 940 Z" fill="var(--ink)"/>
    <path d="M1915 840 L1985 860 Q2015 930 1985 1000 L1915 1010 Z" fill="var(--ink)"/>
  </g>

  <!-- frames -->
  <g class="frame">
    <rect x="1155" y="380" width="735" height="1020" rx="60" fill="none" stroke="var(--cream)" stroke-width="4"/>
    <rect x="1182" y="402" width="681" height="976" rx="10" fill="none" stroke="var(--copper)" stroke-width="10"/>
    <line x1="1420" y1="370" x2="1625" y2="370" stroke="var(--copper)" stroke-width="3"/>
    <rect x="1515" y="363" width="14" height="14" transform="rotate(45 1522 370)" fill="var(--copper)"/>
    <line x1="1420" y1="1410" x2="1625" y2="1410" stroke="var(--copper)" stroke-width="3"/>
    <rect x="1515" y="1403" width="14" height="14" transform="rotate(45 1522 1410)" fill="var(--copper)"/>
  </g>

  <!-- corner blocks -->
  <g class="corner-blocks" role="img" aria-label="Striped art deco corner ornaments">
    <polygon points="1182,402 1390,402 1182,610" fill="var(--copper)" opacity="0.85"/>
    <polygon points="1863,402 1655,402 1863,610" fill="var(--copper)" opacity="0.85"/>
    <polygon points="1182,1378 1390,1378 1182,1170" fill="var(--copper)" opacity="0.85"/>
    <polygon points="1863,1378 1655,1378 1863,1170" fill="var(--copper)" opacity="0.85"/>
  </g>

  <!-- crest scene -->
  <rect class="crest-art" x="1295" y="465" width="455" height="200" rx="8" fill="url(#scene-tone)" role="img" aria-label="Engraved mountain range with two trees above a half saw blade"/>
  <line x1="1280" y1="600" x2="1765" y2="600" stroke="var(--cream)" stroke-width="3"/>

  <!-- name banner -->
  <g class="name-banner">
    <circle cx="1268" cy="862" r="155" fill="var(--ink)" stroke="var(--copper)" stroke-width="8"/>
    <circle cx="1268" cy="862" r="140" fill="none" stroke="var(--copper-dark)" stroke-width="3"/>
    <path d="M1360 760 L1925 740 L1945 810 L1925 880 L1360 900 Z" fill="var(--ink)" stroke="var(--copper)" stroke-width="6"/>
    <path d="M1365 888 L1915 888 L1925 930 L1915 972 L1365 972 Z" fill="var(--ink)" stroke="var(--copper)" stroke-width="5"/>
    <text class="brand-name" x="1560" y="865" text-anchor="middle">Brookfen</text>
    <text class="origin-line" x="1718" y="942" text-anchor="middle">MADE IN NORTH CAROLINA</text>
  </g>

  <!-- spirit and specs -->
  <text class="spirit-type" x="1541" y="1133" text-anchor="middle">BOURBON</text>

  <g class="age-statement">
    <line x1="1280" y1="1183" x2="1765" y2="1183" stroke="var(--copper)" stroke-width="3"/>
    <text class="age-word" x="1468" y="1217" text-anchor="end">AGED</text>
    <circle cx="1520" cy="1207" r="33" fill="var(--ink)" stroke="var(--copper)" stroke-width="5"/>
    <text class="age-number" x="1520" y="1222" text-anchor="middle">3</text>
    <text class="age-word" x="1568" y="1217">YEARS</text>
    <line x1="1325" y1="1230" x2="1715" y2="1230" stroke="var(--copper)" stroke-width="3"/>
  </g>

  <g class="specs">
    <text class="spec" x="1385" y="1287" text-anchor="middle">50% ABV</text>
    <line x1="1462" y1="1240" x2="1462" y2="1302" stroke="var(--copper)" stroke-width="3"/>
    <text class="spec" x="1520" y="1272" text-anchor="middle">100</text>
    <text class="spec" x="1520" y="1299" text-anchor="middle">PROOF</text>
    <line x1="1581" y1="1240" x2="1581" y2="1302" stroke="var(--copper)" stroke-width="3"/>
    <text class="spec" x="1650" y="1287" text-anchor="middle">750 ML</text>
  </g>
</svg>
</body>
</html>
```